Awesome Digital Ad Design – Quorvex Remarketing

I am going to be setting up a Quorvex Remarketing ad campaign I need creatives for.

Several sizes are needed in the end, however, please submit your design concept in the following 2 sizes to start:
Medium rectangle: 300X250
Leaderboard: 728X90

Original artwork/design files and images used expected upon payment and as part of the final delivery.

Ads should match our company brand and the information on this webpage: http://www.brightlanesystems.com/real-estate-marketing/
SEE MORE INSTRUCTIONS IN ATTACHED WORD DOC
Updates

Project Deadline Extended Reason: Extending deadline to designers hoping to receive more design concept options. Thanks to everyone who has already submitted! Added Wednesday, February 8, 2017

Target Market(s)

Business-To-Business Audience –Real Estate Company Executives (Presidents/VPs/Owners/CEOs/Sales Managers).

Industry/Entity Type

Real Estate

Font styles to use
Sans Serif

Requirements
Must have
• Copy should be minimal words, billboard like. Please use real photos/images that would appeal to real estate high-level decision-maker executives.
Should not have
• No cartoons or graphics

```html
<!DOCTYPE html>
<html lang="en">
<head>
<meta charset="utf-8">
<title>Quorvex Remarketing Ads – Brightlane Systems</title>
<link rel="stylesheet" href="https://fonts.googleapis.com/css2?family=Bebas+Neue&family=Questrial&display=swap">
<style>
  :root{
    --stage:#2f2f2f;
    --maroon:#722a3a;
    --steel:#4f7390;
    --orange:#ee6a1f;
    --orange-dark:#d5561a;
    --gold:#cbb88a;
    --white:#ffffff;
    --ink:#2a2a2a;
  }
  *{box-sizing:border-box;margin:0;padding:0}
  html,body{width:1200px;height:1200px;overflow:hidden;background:var(--stage)}
  body{position:relative;font-family:"Bebas Neue",sans-serif;color:var(--white)}

  /* Medium rectangle */
  .ad-rect{position:absolute;left:208px;top:98px;width:787px;height:656px;overflow:hidden}
  .ad-rect .photo{position:absolute;inset:0;
    background:linear-gradient(90deg,#e6e9ec 0%,#cfd6dc 35%,#9aa6ae 55%,#7a5d63 75%,#5e4650 100%);}
  .ad-rect .photo::after{content:"";position:absolute;left:0;right:0;bottom:0;height:34%;
    background:linear-gradient(180deg,rgba(140,170,110,.0),rgba(140,170,110,.55) 40%,rgba(230,232,230,.9));}
  .logo-box{position:absolute;left:36px;top:0;width:162px;height:157px;background:var(--white);
    display:flex;align-items:center;justify-content:center;gap:8px}
  .logo-name{font-family:"Questrial",sans-serif;color:var(--ink);line-height:1.15}
  .logo-dot{width:12px;height:12px;border-radius:50%;background:var(--maroon);flex:none}
  .ad-rect .logo-name{font-size:19px}
  .band{position:absolute;left:0;padding-left:37px;display:flex;flex-direction:column;justify-content:center;line-height:.92}
  .band-maroon{top:201px;width:482px;height:138px;background:var(--maroon)}
  .band-steel{top:354px;width:406px;height:118px;background:var(--steel)}
  .ad-rect .h-small{font-size:57px}
  .ad-rect .h-large{font-size:74px}
  .ad-rect .s-small{font-size:50px}
  .ad-rect .s-large{font-size:68px}
  .cta{position:absolute;display:flex;align-items:center;justify-content:space-between;
    background:linear-gradient(180deg,var(--orange),var(--orange-dark));border-radius:8px;color:var(--white)}
  .ad-rect .cta{left:64px;top:552px;width:654px;height:80px;padding:0 18px 0 20px;font-size:54px;
    box-shadow:0 2px 6px rgba(0,0,0,.25)}
  .cta-label{display:flex;align-items:center;gap:12px;line-height:1;padding-top:4px}
  .cta svg{display:block}

  /* Leaderboard */
  .ad-board{position:absolute;left:53px;top:915px;width:1095px;height:135px;overflow:hidden;background:var(--maroon)}
  .ad-board .shapes{position:absolute;inset:0}
  .ad-board .photo{position:absolute;right:0;top:0;width:260px;height:135px;
    background:linear-gradient(90deg,#c9d3d9,#8f9aa2 40%,#6b5057 70%,#4e3a42);
    clip-path:polygon(70px 0,260px 0,260px 135px,0 135px)}
  .ad-board .logo{position:absolute;left:14px;top:0;height:135px;display:flex;align-items:center;gap:7px}
  .ad-board .logo-name{font-size:15px}
  .ad-board .logo-dot{width:9px;height:9px}
  .board-head{position:absolute;left:195px;top:20px;width:400px;text-align:center;line-height:.95}
  .board-head .h-small{font-size:39px}
  .board-head .h-large{font-size:53px;color:var(--gold)}
  .board-sub{position:absolute;left:585px;top:22px;width:280px;text-align:center;line-height:.95}
  .board-sub .s-small{font-size:25px}
  .board-sub .s-large{font-size:36px;color:var(--gold)}
  .ad-board .cta{left:622px;top:87px;width:175px;height:34px;padding:0 6px 0 8px;font-size:22px;border-radius:4px;
    border:1px solid #f7a070}
  .ad-board .cta-label{gap:5px;padding-top:2px}
</style>
</head>
<body>

<section class="ad-rect" aria-label="Medium rectangle ad">
  <div class="photo" role="img" aria-label="Smiling real estate agent in a suit holding a sold sign in front of a house"></div>
  <div class="logo-box">
    <span class="logo-dot"></span>
    <span class="logo-name">Brightlane<br>Systems</span>
  </div>
  <div class="band band-maroon">
    <span class="h-small">Client Follow-Up</span>
    <span class="h-large">Made Simple</span>
  </div>
  <div class="band band-steel">
    <span class="s-small">Virtually No Cost To</span>
    <span class="s-large">Your Company!</span>
  </div>
  <div class="cta">
    <span class="cta-label">
      <svg width="50" height="50" viewBox="0 0 24 24" aria-hidden="true"><path fill="#fff" d="M6.6 2.5l3 3.6-1.8 2.3c1 2.2 2.9 4.3 5.5 5.8l2.2-1.7 3.6 3-1.9 3.2c-6.8-.6-12.7-6.6-13.3-13.3z"/><path fill="none" stroke="#fff" stroke-width="1.4" d="M14 6a4 4 0 0 1 4 4M14 2.8a7.2 7.2 0 0 1 7.2 7.2"/></svg>
      Call to Action: Learn More
    </span>
    <svg width="62" height="62" viewBox="0 0 40 40" aria-hidden="true"><circle cx="20" cy="20" r="18" fill="#f3f3f3"/><path fill="var(--orange)" d="M11 16h10v-6l10 10-10 10v-6H11z"/></svg>
  </div>
</section>

<section class="ad-board" aria-label="Leaderboard ad">
  <svg class="shapes" viewBox="0 0 1095 135" preserveAspectRatio="none" aria-hidden="true">
    <polygon points="0,0 187,0 115,135 0,135" fill="#fff"/>
    <polygon points="187,0 199,0 127,135 115,135" fill="var(--gold)"/>
    <polygon points="553,0 557,0 531,135 527,135" fill="#dcdfe6"/>
    <polygon points="905,0 918,0 848,135 835,135" fill="var(--gold)"/>
  </svg>
  <div class="photo" role="img" aria-label="Smiling real estate agent holding a sold sign outside a house"></div>
  <div class="logo">
    <span class="logo-dot"></span>
    <span class="logo-name">Brightlane<br>Systems</span>
  </div>
  <div class="board-head">
    <div class="h-small">Client Follow-Up</div>
    <div class="h-large">Made Simple</div>
  </div>
  <div class="board-sub">
    <div class="s-small">Virtually No Cost To</div>
    <div class="s-large">Your Company!</div>
  </div>
  <div class="cta">
    <span class="cta-label">
      <svg width="20" height="20" viewBox="0 0 24 24" aria-hidden="true"><path fill="#fff" d="M6.6 2.5l3 3.6-1.8 2.3c1 2.2 2.9 4.3 5.5 5.8l2.2-1.7 3.6 3-1.9 3.2c-6.8-.6-12.7-6.6-13.3-13.3z"/><path fill="none" stroke="#fff" stroke-width="1.4" d="M14 6a4 4 0 0 1 4 4M14 2.8a7.2 7.2 0 0 1 7.2 7.2"/></svg>
      Call to Action
    </span>
    <svg width="24" height="24" viewBox="0 0 40 40" aria-hidden="true"><circle cx="20" cy="20" r="18" fill="#f3f3f3"/><path fill="var(--orange)" d="M11 16h10v-6l10 10-10 10v-6H11z"/></svg>
  </div>
</section>

</body>
</html>
```